Business Cards and label design needed!

I am a metalsmith, working in sterling silver, brass and moving slowly into adding some gold accent pieces. I also use patinas to add color to brass pieces. The peacock feather is used in my packaging, as both a label and tissue paper. I am attaching what I am currently using, and printing at home, but I need a design that I can have professionally printed. My website is www.willowharborcrafts.com
Target Market(s)
Established Professionals, Independent thinkers, Art donors, Artist supporters
Industry/Entity Type
Jewelry
Contact Information for Business Card
I would like a business card with the basic contact information, including Facebook and Instagram. I currently use a peacock feather and would like to continue that. I like to use turquoise, Tiffany blue and colors in that direction. I am open to other suggestions. I would like to be able to transfer the design to oval labels as well.
Font styles to use
Other font styles liked:
- Garamond or other fonts that have a slight script that is easy to read
Look and feel

```html
<!DOCTYPE html>
<html lang="en">
<head>
<meta charset="UTF-8">
<title>Willow Harbor Crafts – Business Card</title>
<link href="https://fonts.googleapis.com/css2?family=Cormorant+Garamond:wght@500&family=Montserrat:wght@400;600;700&display=swap" rel="stylesheet">
<style>
  :root {
    --backdrop: #b9b9b9;
    --card-paper: #ececec;
    --teal: #23998f;
    --teal-text: #2a9a8f;
    --ink: #4a4a4a;
    --ink-soft: #5a5a5a;
    --rule: #a8a8a8;
    --oval: #ebebeb;
    --mark: #b08a4a;
    --white: #ffffff;
  }
  * { margin: 0; padding: 0; box-sizing: border-box; }
  html, body { width: 1200px; height: 1116px; overflow: hidden; }
  body { background: var(--backdrop); position: relative; }

  .card {
    position: absolute;
    top: 409px;
    width: 540px;
    height: 298px;
    box-shadow: 0 2px 6px rgba(0,0,0,0.18);
  }
  .card--front { left: 40px; background: var(--card-paper); }
  .card--back { left: 620px; background: var(--teal); }

  .front__brand {
    position: absolute; top: 66px; left: 0; width: 100%;
    text-align: center;
    font-family: "Cormorant Garamond", serif;
    font-weight: 500;
    font-size: 36px;
    color: var(--teal-text);
  }
  .front__person {
    position: absolute; top: 150px; left: 0; width: 100%;
    text-align: center;
    font-family: "Montserrat", sans-serif;
    font-weight: 700;
    font-size: 20px;
    color: var(--ink);
  }
  .front__rule {
    position: absolute; top: 191px; left: 254px;
    width: 32px; height: 1px; background: var(--rule);
  }
  .front__contact {
    position: absolute; top: 203px; left: 0; width: 100%;
    text-align: center;
    font-family: "Montserrat", sans-serif;
    font-weight: 400;
    font-size: 14.5px;
    line-height: 21px;
    color: var(--ink-soft);
  }

  .back__oval {
    position: absolute; left: 62px; top: 75px;
    width: 416px; height: 150px;
    border-radius: 50%;
    background: var(--oval);
  }
  .back__mark {
    position: absolute; left: 249px; top: 90px;
    width: 42px; height: 42px; border-radius: 50%;
    background: var(--mark);
  }
  .back__brand {
    position: absolute; top: 148px; left: 0; width: 100%;
    text-align: center;
    font-family: "Cormorant Garamond", serif;
    font-weight: 500;
    font-size: 34px;
    color: var(--teal-text);
  }
  .back__web {
    position: absolute; top: 248px; left: 0; width: 100%;
    text-align: center;
    font-family: "Montserrat", sans-serif;
    font-weight: 600;
    font-size: 13px;
    letter-spacing: 1.6px;
    color: var(--white);
  }
</style>
</head>
<body>
  <section class="card card--front">
    <h1 class="front__brand">Willow Harbor Crafts</h1>
    <p class="front__person">Marla QUINN</p>
    <div class="front__rule"></div>
    <p class="front__contact">555.204.7316<br>hello.willowharbor@gmail.com</p>
  </section>

  <section class="card card--back">
    <div class="back__oval"></div>
    <div class="back__mark"></div>
    <p class="back__brand">Willow Harbor Crafts</p>
    <p class="back__web">www.willowharborcrafts.com</p>
  </section>
</body>
</html>
```